EPIC, awesome, creative business card needed - get involved!

I'm launching a boutique, exclusive Property Management real estate agency in Sydney early next year.
The name of the agency will be called "Quartz Hill Lane" - it's a play on "chase the silver pebble trail" to wealth. The Quartz Hill Lane signifies wealth through property investment.
My business will offer management of investment properties (ie Property Management).
The difference with Quartz Hill Lane and other agencies is the business will be run by one of Australia's leading property investment experts, and also one of Australia's leading property managers.
It will be exclusively for high net worth properties and individuals, so the business card needs to be extremely sharp, slick and relatively simple.
The information I want on the card is as follows
Nolan Pryce - Director
M: 0412 967 154
P: 9735 6021
E: nolan@quartzhilllane.net.au
W: quartzhilllane.net.au
I'm happy with the red from the logo, black - no yellows or funky colors. I want this to be a super corporate and slick business card to match the high end nature of the business.
Good luck everyone, and please ask questions for clarification.

```html
<!DOCTYPE html>
<html lang="en">
<head>
<meta charset="utf-8">
<title>Quartz Hill Lane – Business Card</title>
<link rel="stylesheet" href="https://fonts.googleapis.com/css2?family=Barlow:wght@400;500;600&display=swap">
<style>
  :root {
    --stage: #d6d6d6;
    --card-dark: #231f20;
    --brand-red: #ec1c24;
    --text-light: #c9c9c9;
    --text-white: #ffffff;
    --text-ink: #231f20;
  }
  * { margin: 0; padding: 0; box-sizing: border-box; }
  html, body { width: 1200px; height: 487px; overflow: hidden; }
  body {
    position: relative;
    background: var(--stage);
    font-family: "Barlow", Arial, sans-serif;
  }
  .card-shapes { position: absolute; inset: 0; }
  .card-front-shape { fill: var(--card-dark); }
  .card-back-shape { fill: var(--brand-red); }

  .brand-panel {
    position: absolute;
    left: 118px; top: 138px;
    width: 173px; height: 210px;
    background: var(--brand-red);
    padding: 26px 0 0 26px;
  }
  .brand-name {
    color: var(--text-white);
    font-weight: 600;
    font-size: 39px;
    line-height: 50px;
    text-transform: uppercase;
    letter-spacing: 0;
  }

  .contact { position: absolute; left: 318px; color: var(--text-light); font-size: 14px; line-height: 16px; }
  .person-name { top: 183px; color: var(--brand-red); font-weight: 500; text-transform: uppercase; letter-spacing: 0.3px; }
  .person-role { top: 199px; }
  .contact-line { display: flex; align-items: flex-start; gap: 8px; }
  .contact-line svg { width: 12px; height: 12px; fill: var(--brand-red); flex: none; margin-top: 2px; }
  .contact-line .no-icon { width: 12px; flex: none; }
  .contact-digital { top: 255px; }
  .contact-office { top: 303px; }

  .web-address {
    position: absolute;
    left: 614px; width: 512px; top: 233px;
    text-align: center;
    font-size: 16px;
    color: var(--text-ink);
  }
  .web-address strong { color: var(--text-white); font-weight: 600; }
</style>
</head>
<body>
  <svg class="card-shapes" width="1200" height="487" viewBox="0 0 1200 487" aria-hidden="true">
    <path class="card-front-shape" d="M75 98 H540 V146 H585 V390 H75 Z"/>
    <path class="card-back-shape" d="M614 146 H660 V98 H1126 V390 H614 Z"/>
  </svg>

  <section class="card-front">
    <div class="brand-panel">
      <p class="brand-name">Quartz<br>Hill<br>Lane</p>
    </div>

    <p class="contact person-name">Nolan Pryce</p>
    <p class="contact person-role">Director</p>

    <div class="contact contact-digital">
      <p class="contact-line">
        <svg viewBox="0 0 12 12"><path d="M0 2h12v8H0z M1 3v.6L6 7l5-3.4V3z" fill-rule="evenodd"/></svg>
        <span>nolan@quartzhilllane.net.au</span>
      </p>
      <p class="contact-line">
        <svg viewBox="0 0 12 12"><path d="M3 0h6v12H3z M4 1.5v8h4v-8z" fill-rule="evenodd"/></svg>
        <span>0412 967 154</span>
      </p>
    </div>

    <div class="contact contact-office">
      <p class="contact-line">
        <svg viewBox="0 0 12 12"><path d="M6 0a4 4 0 0 1 4 4c0 3-4 8-4 8S2 7 2 4a4 4 0 0 1 4-4zm0 2.5a1.5 1.5 0 1 0 0 3 1.5 1.5 0 0 0 0-3z"/></svg>
        <span>0101 Avenue, Suite No. 123,</span>
      </p>
      <p class="contact-line">
        <span class="no-icon"></span>
        <span>Your City, Country</span>
      </p>
      <p class="contact-line">
        <svg viewBox="0 0 12 12"><circle cx="6" cy="6" r="6"/><path d="M3.5 3h1.6l.6 1.6-.9.7a4 4 0 0 0 1.9 1.9l.7-.9 1.6.6v1.6c-3 .3-5.8-2.5-5.5-5.5z" fill="#231f20"/></svg>
        <span>9735 6021</span>
      </p>
    </div>
  </section>

  <section class="card-back">
    <p class="web-address">www.<strong>QuartzHillLane</strong>.net.au</p>
  </section>
</body>
</html>
```